Roadside building business signage for a holistic health clinic.

Replace signs as shown in the attached file. They are perforated stickers that go on the windows as shown. Looking for something that has our logo and says the name of the practice with logo (Fernbrook Health & Wellness) also boldly says Acupuncture, IV Vitamins, and Holistic Health.
Possibly our phone number as well 318-627-5194
Updates

Please don't use pink except the logo. Earthy, organic tone colors appreciated.

Need of eye catching window signage of a holistic clinic on a brick building. Pink, purple, sage green, white color. Logo is pink on a white background. Please don't overload with too much pink. Words to include are "Fernbrook Health and Wellness(name of business)", "Direct Primary Care", " Medical acupuncture", "IV Vitamin Therapy", "fernbrookcare-example.com","318-627-5194".

Target Market(s)

People will see in their cars passing by the building. Busy roadside so need to be visible while passing in fast speed.

Industry/Entity Type

Health & Wellness

Font styles to use
Sans Serif

Colors

Designer to choose colors to be used in the design.

Requirements
Must have
• On sign must have words Holistic Medicine, Medical Acupuncture, Direct Primary Care and IV vitamins.
Nice to have
• Simple, minimalistic, artistic yet has clear message. White, Black, Violet, Pink (logo), Dark green, Sage green.
Should not have
• Bold colors (red, yellow, blue), same tone colors. Blue waves on the current signage (uploaded file) must go.

```html
<!DOCTYPE html>
<html lang="en">
<head>
<meta charset="utf-8">
<title>Fernbrook Health &amp; Wellness — Window Signage</title>
<link rel="stylesheet" href="https://fonts.googleapis.com/css2?family=Raleway:wght@500;600;700&display=swap">
<style>
  :root {
    --navy: #0a3466;
    --cream: #f7f0e4;
    --cream-light: #fbf8ee;
    --sage: #94a68f;
    --sage-dark: #7f9379;
    --taupe: #8c8275;
    --forest: #0f4a3a;
    --blossom: #e0508f;
    --meadow-light: #dcd9b0;
    --meadow: #bdbc7d;
    --white: #ffffff;
    --panel: 224px;
  }
  * { box-sizing: border-box; margin: 0; padding: 0; }
  html, body { width: 1200px; height: 2592px; overflow: hidden; }
  body {
    background: var(--navy);
    font-family: "Raleway", sans-serif;
    position: relative;
  }
  .signage {
    position: absolute;
    left: 20px;
    top: 950px;
    width: 1160px;
    height: 692px;
  }
  .pane {
    position: absolute;
    width: var(--panel);
    height: var(--panel);
    overflow: hidden;
    background: linear-gradient(135deg, var(--cream-light) 0%, var(--cream) 55%, #f2e9da 100%);
  }
  .pane--arch-left { border-top-left-radius: 100% 100%; }
  .pane--arch-right { border-top-right-radius: 100% 100%; }

  .col-1 { left: 0; } .col-2 { left: 234px; } .col-3 { left: 468px; }
  .col-4 { left: 702px; } .col-5 { left: 936px; }
  .row-1 { top: 0; } .row-2 { top: 234px; } .row-3 { top: 468px; }

  /* name mark */
  .brand {
    position: absolute; inset: 0;
    display: flex; flex-direction: column; align-items: center; justify-content: center;
    gap: 14px;
  }
  .brand__dot {
    width: 46px; height: 46px; border-radius: 50%;
    background: var(--blossom);
  }
  .brand__name {
    color: var(--forest);
    font-weight: 700;
    font-size: 21px;
    line-height: 1.2;
    letter-spacing: 0.04em;
    text-align: center;
  }

  /* services list */
  .pane--sage { background: linear-gradient(135deg, var(--sage) 0%, var(--sage-dark) 100%); }
  .services {
    position: absolute; left: 34px; right: 34px; top: 34px;
    list-style: none;
    font-weight: 600; font-size: 19px; line-height: 1.1;
    color: var(--taupe);
  }
  .pane--sage .services { color: var(--white); }
  .services li { padding: 7px 0; border-bottom: 1.5px solid currentColor; }
  .services li:last-child { border-bottom: none; }
  .services li:first-child { padding-top: 0; }

  /* contact */
  .contact {
    position: absolute; left: 24px; right: 16px; top: 26px;
    color: var(--taupe);
  }
  .contact__web { font-weight: 600; font-size: 17px; }
  .contact__phone {
    margin-top: 9px;
    display: inline-flex; align-items: center; gap: 8px;
    background: var(--sage); color: var(--white);
    border-radius: 14px; padding: 3px 14px 3px 4px;
    font-weight: 700; font-size: 18px;
  }
  .contact__icon {
    width: 22px; height: 22px; border-radius: 50%;
    background: var(--white);
    display: flex; align-items: center; justify-content: center;
  }

  /* lower meadow band */
  .meadow {
    position: absolute; left: 0; right: 0; bottom: 0; height: 104px;
    background: linear-gradient(180deg, var(--meadow-light) 0%, #cfcd98 45%, var(--meadow) 100%);
  }
</style>
</head>
<body>
  <main class="signage" aria-label="Fernbrook Health &amp; Wellness window signage layout">
    <!-- arch row -->
    <div class="pane pane--arch-left col-3 row-1"></div>
    <div class="pane pane--arch-right col-4 row-1"></div>

    <!-- middle row -->
    <div class="pane col-2 row-2">
      <div class="brand">
        <span class="brand__dot"></span>
        <p class="brand__name">Fernbrook<br>Health &amp; Wellness</p>
      </div>
    </div>
    <div class="pane pane--sage col-3 row-2">
      <ul class="services">
        <li>Medical<br>Acupuncture</li>
        <li>IV Vitamins</li>
        <li>Holistic Health</li>
        <li>Direct<br>Primary Care</li>
      </ul>
    </div>
    <div class="pane col-4 row-2">
      <div class="brand">
        <span class="brand__dot"></span>
        <p class="brand__name">Fernbrook<br>Health &amp; Wellness</p>
      </div>
    </div>
    <div class="pane col-5 row-2">
      <ul class="services">
        <li>Medical<br>Acupuncture</li>
        <li>IV Vitamins</li>
        <li>Holistic Health</li>
        <li>Direct<br>Primary Care</li>
      </ul>
    </div>

    <!-- bottom row -->
    <div class="pane col-1 row-3">
      <div class="meadow" role="img" aria-label="Soft layered green hill waves"></div>
    </div>
    <div class="pane col-2 row-3">
      <div class="meadow" role="img" aria-label="Soft layered green hill waves"></div>
    </div>
    <div class="pane col-3 row-3">
      <div class="contact">
        <p class="contact__web">fernbrookcare-example.com</p>
        <p class="contact__phone">
          <span class="contact__icon">
            <svg width="12" height="12" viewBox="0 0 24 24" aria-hidden="true"><path fill="#94a68f" d="M6.6 10.8a15.1 15.1 0 0 0 6.6 6.6l2.2-2.2a1 1 0 0 1 1-.25 11.4 11.4 0 0 0 3.6.57 1 1 0 0 1 1 1V20a1 1 0 0 1-1 1A17 17 0 0 1 3 4a1 1 0 0 1 1-1h3.5a1 1 0 0 1 1 1c0 1.25.2 2.45.57 3.57a1 1 0 0 1-.25 1z"/></svg>
          </span>
          318-627-5194
        </p>
      </div>
      <div class="meadow" role="img" aria-label="Soft layered green hill waves"></div>
    </div>
    <div class="pane col-4 row-3">
      <div class="meadow" role="img" aria-label="Soft layered green hill waves"></div>
    </div>
    <div class="pane col-5 row-3">
      <div class="contact">
        <p class="contact__web">fernbrookcare-example.com</p>
        <p class="contact__phone">
          <span class="contact__icon">
            <svg width="12" height="12" viewBox="0 0 24 24" aria-hidden="true"><path fill="#94a68f" d="M6.6 10.8a15.1 15.1 0 0 0 6.6 6.6l2.2-2.2a1 1 0 0 1 1-.25 11.4 11.4 0 0 0 3.6.57 1 1 0 0 1 1 1V20a1 1 0 0 1-1 1A17 17 0 0 1 3 4a1 1 0 0 1 1-1h3.5a1 1 0 0 1 1 1c0 1.25.2 2.45.57 3.57a1 1 0 0 1-.25 1z"/></svg>
          </span>
          318-627-5194
        </p>
      </div>
      <div class="meadow" role="img" aria-label="Soft layered green hill waves"></div>
    </div>
  </main>
</body>
</html>
```